High Tech Software Company Needs MOVIE POSTER

We need a poster design for theme for our 2016 kick off event for the sales team. Our software company is based in TORONTO & BOSTON and we essentially do 'crowdsourcing' for referrals, references, and reviews.

Our domain is www.brackenvale.com check it out to see our culture and our logo to be used in the design.

The THEME of our kick off is "ALL IN!" we would like to see the design use our logo and be creative and AWESOME potentially a poster that represents a movie? The design needs to inspire people, it needs to get them excited.

its only for internal use there is no issue about copywrite

Target Market(s)

These posters will be in all of our offices, Toronto, Boston, Palo Alto, and San Fran

Industry/Entity Type

Movie

Requirements
Must have
• The theme on it, "All In". it must be a motivating image. it is a theme commonly used in poker, "I'm All in!" pushing all their poker chips into the game. Check out some images on that. using the brackenvale logo (in the poker chips?) Maybe the poker table with the brackenvale logo? We will supply the names but the poster should also have the MOVIE theme see attached poster for making it "movie like" with names and the credits that are commonly found on movie posters. THE ATTACHMENT IS FROM A PREVIOUS CONTEST. SHOWN STRICTLY FOR THE MOVIE POSTER THEME CONTENT IS NOT RELEVANT!!!
Nice to have
• Its for a sales team so obviously the "all in" has to be motivating.

```html
<!DOCTYPE html>
<html lang="en">
<head>
<meta charset="utf-8">
<title>All In — Brackenvale Kick Off Poster</title>
<link href="https://fonts.googleapis.com/css2?family=Archivo+Black&family=Nunito:ital,wght@0,800;1,600&family=Oswald:wght@300;400&display=swap" rel="stylesheet">
<style>
  :root {
    --backdrop: #6f7276;
    --night: #0e0c2a;
    --indigo: #1d1a4d;
    --violet: #3a2f6e;
    --chip-red: #8a1a2a;
    --chip-blue: #2a2e8c;
    --skin: #b98a78;
    --white: #ffffff;
    --soft: #d9dcef;
    --brand-blue: #1ea2dc;
    --flare: #9fd0ff;
  }
  * { margin: 0; padding: 0; box-sizing: border-box; }
  html, body { width: 1200px; height: 1000px; overflow: hidden; }
  body { background: var(--backdrop); position: relative; }

  .poster {
    position: absolute; left: 278px; top: 26px;
    width: 642px; height: 947px; overflow: hidden;
    background: linear-gradient(180deg, var(--indigo) 0%, var(--night) 55%, #15133a 85%, #1c2a66 100%);
  }
  .poster__photo {
    position: absolute; left: 0; top: 0; width: 642px; height: 560px;
    background:
      radial-gradient(ellipse 120px 110px at 230px 170px, var(--skin) 0%, rgba(185,138,120,0) 100%),
      radial-gradient(ellipse 70px 60px at 340px 250px, var(--chip-red) 0%, rgba(138,26,42,0) 100%),
      radial-gradient(ellipse 150px 80px at 330px 420px, rgba(200,205,215,.55) 0%, rgba(200,205,215,0) 100%),
      radial-gradient(ellipse 110px 70px at 500px 340px, var(--chip-blue) 0%, rgba(42,46,140,0) 100%),
      linear-gradient(180deg, #241f52 0%, var(--violet) 40%, rgba(14,12,42,0) 100%);
    -webkit-mask-image: linear-gradient(180deg, #000 70%, transparent 100%);
            mask-image: linear-gradient(180deg, #000 70%, transparent 100%);
  }
  .poster__flare {
    position: absolute; left: 0; bottom: 0; width: 642px; height: 120px;
    background: radial-gradient(ellipse 300px 45px at 50% 100%, rgba(220,240,255,.95) 0%, rgba(159,208,255,.5) 40%, rgba(159,208,255,0) 100%);
  }
  .poster__flare-line {
    position: absolute; left: 190px; bottom: 56px; width: 260px; height: 1px;
    background: linear-gradient(90deg, transparent, var(--flare), transparent);
  }

  .brand {
    position: absolute; top: 478px; left: 0; width: 100%;
    display: flex; flex-direction: column; align-items: center;
    font-family: "Nunito", sans-serif; color: var(--white);
  }
  .brand__row { display: flex; align-items: center; gap: 8px; }
  .brand__dot { width: 32px; height: 32px; border-radius: 50%; background: var(--brand-blue); }
  .brand__name { font-weight: 800; font-size: 34px; line-height: 1; letter-spacing: .5px; }
  .brand__tagline { font-weight: 800; font-size: 13px; margin: 2px 0 0 40px; }

  .presents {
    position: absolute; top: 534px; left: 0; width: 100%;
    display: flex; align-items: center; justify-content: center; gap: 14px;
    font-family: "Nunito", sans-serif; font-style: italic; font-weight: 600;
    font-size: 17px; color: var(--soft);
  }
  .presents__rule { width: 150px; height: 1px; background: rgba(217,220,239,.45); }

  .title { position: absolute; left: 0; top: 560px; }

  .credits {
    position: absolute; top: 766px; left: 0; width: 100%;
    font-family: "Oswald", sans-serif; font-weight: 300; color: var(--soft);
    display: flex; flex-direction: column; align-items: center; gap: 3px;
  }
  .credits__line { display: flex; align-items: center; gap: 6px; font-size: 17px; line-height: 19px; white-space: nowrap; }
  .credits__role { font-size: 7.5px; line-height: 7px; text-align: center; text-transform: lowercase; }
  .credits__role--inline { font-size: 9px; }
</style>
</head>
<body>
  <main class="poster">
    <div class="poster__photo" role="img" aria-label="Photo of a hand pushing a stack of red poker chips beside tall stacks of white, green and blue chips on a dark table"></div>
    <div class="poster__flare"></div>
    <div class="poster__flare-line"></div>

    <div class="brand">
      <div class="brand__row">
        <span class="brand__dot"></span>
        <span class="brand__name">brackenvale</span>
      </div>
      <span class="brand__tagline">advocate marketing experts</span>
    </div>

    <div class="presents">
      <span class="presents__rule"></span>presents<span class="presents__rule"></span>
    </div>

    <svg class="title" width="642" height="190" viewBox="0 0 642 190" aria-label="All In">
      <defs>
        <linearGradient id="chrome" x1="0" y1="0" x2="0" y2="1">
          <stop offset="0" stop-color="#c9b6d6"/>
          <stop offset=".35" stop-color="#e4e0ec"/>
          <stop offset=".55" stop-color="#f4f4f8"/>
          <stop offset=".58" stop-color="#7f8296"/>
          <stop offset=".8" stop-color="#4d5070"/>
          <stop offset="1" stop-color="#b7bdd8"/>
        </linearGradient>
      </defs>
      <text x="321" y="177" text-anchor="middle" textLength="520" lengthAdjust="spacingAndGlyphs"
            font-family="'Archivo Black', sans-serif" font-size="232"
            fill="url(#chrome)" stroke="#f2f2f8" stroke-width="2">ALL IN</text>
    </svg>

    <div class="credits">
      <div class="credits__line">BRIGHTHOLLOW <span class="credits__role credits__role--inline">in association with</span> MOSSGATE <span class="credits__role credits__role--inline">and</span> TERNWICK PRODUCTIONS <span class="credits__role credits__role--inline">presents a film by</span> MIRELA SOTANO</div>
      <div class="credits__line">“LOUD SIGNAL” <span class="credits__role">executive<br>producers</span> ANA ROOKE LINA FARROW OWEN DALE <span class="credits__role">director of<br>photography</span> PAVEL MOSS <span class="credits__role credits__role--inline">editor</span> TOMAS REINER</div>
      <div class="credits__line"><span class="credits__role">original<br>score</span> ERIK VANCE <span class="credits__role">associate<br>producers</span> NORA HALLOW TOMAS REINER GRANT PELLOW</div>
      <div class="credits__line"><span class="credits__role credits__role--inline">introducing</span> COLE BRANDT &nbsp;<span class="credits__role credits__role--inline">co-producer</span> ILSE MORAND &nbsp;<span class="credits__role">produced and<br>directed by</span> MIRELA SOTANO</div>
    </div>
  </main>
</body>
</html>
```